Upsell Vertical Banner Ad Design For B2B Marketing Agency Vertical 768px × 1180px IS THE SIZE

I need a banner made for my website www.brightlanepromotionhub.biz This banner will be an upsell advertisement for after someone signs up for my monthly program. When they login to their account for the 1st time I will give them the chance to upgrade their account to our annual program with just one click.

this is a page that upsells it currently to give you an idea how we market ourselves:
https://tlpx.pagevault-example.com/page/tlp-annual-upsell

Use this content:

Are You Ready To Commit To Taking Your Business To The Next Level?

Because We're In This For The Long-Haul and Dedicated To Your Success...

Save $300 By Upgrading To An Annual Membership And Pay Only $74/mth

((BUTTON))Yes, Upgrade My Plan Right Now!

*Must prepay the full year at only $898/yr!

Target Market(s)

business owners

Industry/Entity Type

Marketing

Requirements
Must have
• 768px × 1180px IS THE SIZE vertical

Use this content:

Nice to have
• Use this content:

Should not have
• Use this content:

```html
<!DOCTYPE html>
<html lang="en">
<head>
<meta charset="utf-8">
<title>Annual Upgrade Banner</title>
<link rel="stylesheet" href="https://fonts.googleapis.com/css2?family=Arimo:wght@400&family=Oswald:wght@500;700&family=Poppins:ital,wght@0,400;1,200;1,500&display=swap">
<style>
  :root {
    --stage: #a3a19d;
    --navy-top: #252a4b;
    --navy-bottom: #0a0e33;
    --navy-deep: #070b30;
    --accent-blue: #0014b4;
    --accent-green: #4caf50;
    --cta: #f23300;
    --white: #ffffff;
    --soft-white: #e8e9f0;
    --stone-light: #e4e3e1;
    --stone-dark: #c9c8c5;
  }
  * { margin: 0; padding: 0; box-sizing: border-box; }
  html, body {
    width: 1200px; height: 1200px; overflow: hidden;
    background: var(--stage);
  }
  .banner {
    position: absolute; left: 242px; top: 50px;
    width: 718px; height: 1102px; overflow: hidden;
    color: var(--white);
  }
  .banner__backdrop {
    position: absolute; inset: 0;
    background: linear-gradient(170deg, var(--navy-top) 0%, #161b40 45%, var(--navy-bottom) 100%);
  }
  .banner__lower {
    position: absolute; left: 0; right: 0; top: 786px; bottom: 0;
    background: var(--navy-deep);
    border-top: 1px solid #1d2250;
  }
  .corner { position: absolute; top: 0; }
  .corner--blue { left: 0; }
  .corner--green { right: 0; }
  .headline-intro {
    position: absolute; left: 66px;
    font-family: "Arimo", Arial, sans-serif; font-weight: 400;
    font-size: 44px; line-height: 1; letter-spacing: 0.5px;
    text-transform: uppercase;
  }
  .headline-intro--one { top: 73px; }
  .headline-intro--two { top: 137px; }
  .headline-main {
    position: absolute; left: 64px;
    font-family: "Oswald", sans-serif; font-weight: 700;
    font-size: 90px; line-height: 1; letter-spacing: 1px;
    text-transform: uppercase;
  }
  .headline-main--one { top: 190px; }
  .headline-main--two { top: 292px; }
  .tagline {
    position: absolute; left: 66px; top: 421px;
    font-family: "Poppins", sans-serif; font-style: italic;
    font-size: 23px; line-height: 33px; letter-spacing: -0.6px;
  }
  .tagline__light { font-weight: 200; display: block; color: var(--soft-white); }
  .tagline__strong { font-weight: 500; display: block; }
  .offer {
    position: absolute; left: 66px; top: 518px;
    font-family: "Oswald", sans-serif; font-weight: 500;
    font-size: 31px; line-height: 45px; letter-spacing: 0.2px;
    text-transform: uppercase;
  }
  .cta {
    position: absolute; left: 65px; top: 646px;
    width: 348px; height: 45px;
    background: var(--cta);
    font-family: "Poppins", sans-serif; font-weight: 400;
    font-size: 21px; line-height: 45px; text-align: center;
    letter-spacing: -0.3px;
  }
  .footnote {
    position: absolute; left: 66px; top: 734px;
    font-family: "Arimo", Arial, sans-serif; font-weight: 400;
    font-size: 22px; line-height: 1; letter-spacing: 0.1px;
    text-transform: uppercase;
  }
  .ring { position: absolute; left: 0; top: 0; }
</style>
</head>
<body>
  <main class="banner">
    <div class="banner__backdrop" role="img" aria-label="Dark navy-tinted photo of hands typing on a laptop keyboard"></div>
    <div class="banner__lower"></div>

    <svg class="corner corner--blue" width="82" height="92" viewBox="0 0 82 92" aria-hidden="true">
      <polygon points="0,0 82,0 0,92" fill="var(--accent-blue)"/>
    </svg>
    <svg class="corner corner--green" width="211" height="57" viewBox="0 0 211 57" aria-hidden="true">
      <polygon points="0,0 211,0 211,57" fill="var(--accent-green)"/>
    </svg>

    <h1>
      <span class="headline-intro headline-intro--one">Are You Ready To</span>
      <span class="headline-intro headline-intro--two">Commit To Taking Your</span>
      <span class="headline-main headline-main--one">Business To The</span>
      <span class="headline-main headline-main--two">Next Level?</span>
    </h1>

    <p class="tagline">
      <span class="tagline__light">Because We're In This For The Long-Haul and</span>
      <span class="tagline__strong">Dedicated To Your Success...</span>
    </p>

    <p class="offer">Save $300 By Upgrading To An<br>Annual Membership And Pay Only $74/ Month</p>

    <div class="cta">Yes, Upgrade My Plan Right Now</div>

    <p class="footnote">*Must Prepay The Full Year At Only&nbsp; $898/Year!</p>

    <svg class="ring" width="718" height="1102" viewBox="0 0 718 1102">
      <defs>
        <linearGradient id="stone" x1="0" y1="0" x2="0" y2="1">
          <stop offset="0" stop-color="var(--stone-light)"/>
          <stop offset="1" stop-color="var(--stone-dark)"/>
        </linearGradient>
      </defs>
      <circle cx="359" cy="1107" r="325" fill="none" stroke="var(--accent-green)" stroke-width="1.5" stroke-dasharray="9 8"/>
      <circle cx="359" cy="1107" r="300" fill="url(#stone)" role="img" aria-label="Photo of a businessman walking up a pale concrete staircase"/>
    </svg>
  </main>
</body>
</html>
```